Marrow Business Cards

Front of business card will have logo, name, address, & telephone number. Back of card will have a list of services provided - Roads, Substation Pads, Temporary Pads, Site Pads, Land Leveling, Powerline Row Cleaning, Land Clearing, Gates, Fencing, Construction Entrances, Excavation, Trenching, Underground Utilities, Directional Boring, Pile Driving. We are a construction company that uses heavy equipment like bulldozers, motor graders/blades, dump trucks, backhoes, hydro axes, & skid loaders. We build roads, pads, & install electric utility lines & waterlines underground. This logo is new. The word "Construction" can be smaller as uploaded 2 example edited logos. We will be using this card design for many employees.
Target Market(s)
Industrial Electric Powerline, Wind Turbine, Solar Panel, & Water Utility companies.
Contact Information for Business Card
Name/Position - Dorian Quale - Owner
Address: 4837 Hollis Creek Rd
Brayton, OK 73521
Phone number - (580) 418-2906

```html
<!DOCTYPE html>
<html lang="en">
<head>
<meta charset="UTF-8">
<title>Marrow Business Cards</title>
<link href="https://fonts.googleapis.com/css2?family=Arimo:wght@400;700&display=swap" rel="stylesheet">
<style>
  :root {
    --stage: #1b1b1b;
    --maroon: #3d1520;
    --maroon-ink: #3a1219;
    --paper: #ffffff;
    --ink-grey: #555555;
    --rule-grey: #7a7a7a;
    --rule-soft: rgba(255,255,255,0.35);
  }
  * { box-sizing: border-box; margin: 0; padding: 0; }
  html, body {
    width: 1200px; height: 900px; overflow: hidden;
    background: var(--stage);
    font-family: "Arimo", Arial, sans-serif;
  }
  .stage {
    width: 1200px; height: 900px;
    display: flex; flex-direction: column; align-items: center; justify-content: center;
    gap: 40px;
  }
  .card {
    width: 660px; height: 377px;
    box-shadow: 0 14px 30px rgba(0,0,0,0.55);
    position: relative;
    overflow: hidden;
  }
  /* Back card */
  .card-back {
    background: var(--maroon);
    color: var(--paper);
    display: flex; flex-direction: column; align-items: center;
    padding-top: 60px;
    text-align: center;
  }
  .brand-back {
    display: flex; align-items: center; gap: 12px;
    font-weight: 700; font-size: 52px; letter-spacing: 2px; line-height: 1;
    color: var(--paper);
    margin-bottom: 46px;
  }
  .brand-dot {
    width: 20px; height: 20px; border-radius: 50%; background: var(--paper);
    flex: none;
  }
  .services {
    font-size: 17px; line-height: 1.35;
  }
  .services-rule {
    width: 280px; height: 1px; background: var(--rule-soft);
    margin: 12px auto;
  }
  /* Front card */
  .card-front {
    background: var(--paper);
    display: flex; align-items: center;
    padding-left: 36px;
  }
  .brand-front {
    width: 300px;
    display: flex; flex-direction: column; align-items: center;
    color: var(--maroon-ink);
    margin-top: 90px;
  }
  .brand-front-name {
    display: flex; align-items: center; gap: 12px;
    font-weight: 700; font-size: 50px; letter-spacing: 2px; line-height: 1;
  }
  .brand-front-name .brand-dot { background: var(--maroon-ink); }
  .brand-front-sub {
    font-size: 26px; letter-spacing: 1px; margin-top: 12px;
  }
  .divider {
    width: 1px; height: 160px; background: var(--rule-grey);
    margin-left: 24px;
  }
  .contact {
    padding-left: 30px;
    color: var(--ink-grey);
  }
  .contact-name {
    color: var(--maroon-ink); font-weight: 700; font-size: 22px; letter-spacing: 0.5px;
  }
  .contact-role { font-size: 14px; margin: 2px 0 0 18px; }
  .contact-phone {
    color: var(--maroon-ink); font-weight: 700; font-size: 18px;
    margin: 22px 0 0 18px;
  }
  .contact-address { font-size: 16px; line-height: 1.3; margin: 18px 0 0 18px; }
</style>
</head>
<body>
<main class="stage">
  <section class="card card-back" aria-label="Card back">
    <div class="brand-back"><span class="brand-dot"></span>MARROW</div>
    <p class="services">We are a construction company that uses heavy equipment<br>like bulldozers | motor graders/blades | dump trucks<br>backhoes | hydro axes &amp; skid loaders.</p>
    <div class="services-rule"></div>
    <p class="services">We build roads, pads<br>install electric utility lines &amp; waterlines underground.</p>
  </section>

  <section class="card card-front" aria-label="Card front">
    <div class="brand-front">
      <div class="brand-front-name"><span class="brand-dot"></span>MARROW</div>
      <div class="brand-front-sub">CONSTRUCTION</div>
    </div>
    <div class="divider"></div>
    <div class="contact">
      <p class="contact-name">DORIAN QUALE</p>
      <p class="contact-role">Owner</p>
      <p class="contact-phone">P: (580) 418-2906</p>
      <p class="contact-address">4837 Hollis Creek Rd<br>Brayton, OK 73521</p>
    </div>
  </section>
</main>
</body>
</html>
```